RT Pemberly Electric Yard Sign

Looking to have a yard sign designed that we can place at projects we are working on. Most likely will be 18" H x 24" W but flexible that we can increase the size if necessary. It should include our logo, our phone # 609-555-0147, website rtpemberlyelectric-example.com and slogan, built on integrity, driven by excellence. Colors should match our brand.

```html
<!DOCTYPE html>
<html lang="en">
<head>
<meta charset="utf-8">
<title>RT Pemberly Electric Yard Sign</title>
<link rel="stylesheet" href="https://fonts.googleapis.com/css2?family=Montserrat:wght@600;800&family=Open+Sans:wght@700&family=Source+Serif+4:ital,opsz,wght@1,8..60,700&display=swap">
<style>
  :root {
    --brand-red: #ee1c2e;
    --brand-navy: #0b3466;
    --navy-deep: #082a55;
    --navy-glow: #0f5096;
    --sign-white: #ffffff;
    --backdrop: #e8ebe6;
  }
  * { margin: 0; padding: 0; box-sizing: border-box; }
  html, body {
    width: 1200px;
    height: 1029px;
    overflow: hidden;
    background: var(--backdrop);
  }
  .yard-sign {
    position: absolute;
    left: 20px;
    top: 79.5px;
    width: 1160px;
    height: 870px;
    background: var(--sign-white);
    overflow: hidden;
  }
  .sign-bands {
    position: absolute;
    inset: 0;
    width: 100%;
    height: 100%;
  }
  .brand-mark {
    position: absolute;
    left: 515px;
    top: 40px;
    width: 130px;
    height: 130px;
    border-radius: 50%;
    background: var(--brand-navy);
  }
  .brand-name {
    position: absolute;
    left: 0;
    right: 0;
    top: 208px;
    text-align: center;
    font-family: "Montserrat", sans-serif;
    font-weight: 800;
    font-size: 74px;
    letter-spacing: 1px;
    color: var(--brand-red);
    white-space: nowrap;
    line-height: 1;
  }
  .trade-line {
    position: absolute;
    left: 0;
    right: 0;
    top: 308px;
    text-align: center;
    font-family: "Montserrat", sans-serif;
    font-weight: 800;
    font-size: 40px;
    letter-spacing: 16px;
    padding-left: 16px;
    color: var(--brand-navy);
    white-space: nowrap;
    line-height: 1;
  }
  .trade-rule {
    position: absolute;
    left: 91px;
    top: 358px;
    width: 980px;
    height: 18px;
  }
  .slogan {
    position: absolute;
    left: 0;
    right: 0;
    top: 400px;
    text-align: center;
    font-family: "Source Serif 4", serif;
    font-style: italic;
    font-weight: 700;
    font-size: 47px;
    letter-spacing: -1px;
    color: var(--brand-navy);
    line-height: 1.2;
  }
  .phone-line {
    position: absolute;
    left: 111px;
    top: 529px;
    height: 102px;
    display: flex;
    align-items: center;
    gap: 28px;
  }
  .phone-badge {
    width: 102px;
    height: 102px;
    flex: none;
  }
  .phone-number {
    font-family: "Open Sans", sans-serif;
    font-weight: 700;
    font-size: 128px;
    letter-spacing: -2px;
    color: var(--sign-white);
    line-height: 1;
    white-space: nowrap;
  }
  .website {
    position: absolute;
    left: 0;
    right: 0;
    top: 756px;
    text-align: center;
    font-family: "Montserrat", sans-serif;
    font-weight: 600;
    font-size: 54px;
    color: var(--sign-white);
    line-height: 1.2;
    white-space: nowrap;
  }
</style>
</head>
<body>
  <main class="yard-sign">
    <svg class="sign-bands" viewBox="0 0 1360 1020" preserveAspectRatio="none" aria-hidden="true">
      <defs>
        <radialGradient id="diamond-glow" cx="50%" cy="50%" r="55%">
          <stop offset="0%" stop-color="var(--navy-glow)"/>
          <stop offset="100%" stop-color="var(--navy-deep)"/>
        </radialGradient>
      </defs>
      <polygon class="navy-base" points="0,760 680,850 1360,760 1360,1020 0,1020" fill="var(--brand-navy)"/>
      <polygon class="white-chevron" points="0,752 680,843 1360,752 1360,770 680,862 0,770" fill="var(--sign-white)"/>
      <polygon class="red-band" points="16,610 680,563 1344,610 1344,754 680,843 16,754" fill="var(--brand-red)"/>
      <polygon class="center-diamond" points="440,810 680,768 920,810 680,843" fill="var(--navy-deep)"/>
      <polygon class="center-diamond-inner" points="520,810 680,782 840,810 680,834" fill="url(#diamond-glow)"/>
    </svg>

    <span class="brand-mark"></span>
    <h1 class="brand-name">RT PEMBERLY ELECTRIC</h1>
    <p class="trade-line">Electrical Contractor</p>
    <svg class="trade-rule" viewBox="0 0 980 18" preserveAspectRatio="none" aria-hidden="true">
      <polygon points="0,0 980,0 962,6 18,6" fill="var(--brand-red)"/>
      <rect x="18" y="7" width="944" height="8" fill="var(--brand-navy)"/>
    </svg>

    <p class="slogan">Built on Integrity, Driven by Excellence</p>

    <div class="phone-line">
      <svg class="phone-badge" viewBox="0 0 100 100" aria-hidden="true">
        <circle cx="50" cy="50" r="50" fill="var(--sign-white)"/>
        <path d="M34 26c3-2 6-1 7 2l5 10c1 2 0 5-2 6l-4 3c2 6 7 11 13 14l3-4c1-2 4-3 6-2l10 5c3 1 4 4 2 7l-3 5c-2 3-6 4-10 3-18-5-31-18-36-36-1-4 0-8 3-10z" fill="var(--brand-red)"/>
        <path d="M56 24a22 22 0 0 1 20 20" stroke="var(--brand-red)" stroke-width="4.5" fill="none" stroke-linecap="round"/>
        <path d="M55 34a12 12 0 0 1 11 11" stroke="var(--brand-red)" stroke-width="4.5" fill="none" stroke-linecap="round"/>
      </svg>
      <span class="phone-number">609-555-0147</span>
    </div>

    <p class="website">rtpemberlyelectric-example.com</p>
  </main>
</body>
</html>
```